Silverleaf Rise Accounting Program

size of ad Full: 7” x 9.6”
1- this is for a ladies program so it should appeal to women.
2-however, I do not want any pictures of people in this ad.
3-all the text should be seen and not covered over by graphics.
4-It should be an ad that will draw people's attention and people should look at it and say it looks nice I want to see that ad.
5-I have put all the instructions in yellow in the file below.
6-please leave 1 inch for the footer .
good luck with this project

• no picture or vector of people.

```html
<!DOCTYPE html>
<html lang="en">
<head>
<meta charset="utf-8">
<title>Silverleaf Rise Accounting Program – Open House</title>
<link rel="stylesheet" href="https://fonts.googleapis.com/css2?family=Crimson+Pro:wght@400;600;700&family=Arimo:wght@700&family=Kaushan+Script&display=swap">
<style>
  :root {
    --ink: #3f3f3f;
    --pink: #e8616f;
    --pink-soft: #f4a3aa;
    --yellow: #f5c93a;
    --paper: #ffffff;
    --mist: #f6efee;
  }
  * { margin: 0; padding: 0; box-sizing: border-box; }
  html, body { width: 875px; height: 1200px; overflow: hidden; background: var(--paper); }
  .ad {
    position: relative; width: 875px; height: 1200px; overflow: hidden;
    background: var(--paper);
    font-family: "Crimson Pro", Georgia, serif; color: var(--ink);
  }
  .hero-photo {
    position: absolute; left: 0; top: 0; width: 480px; height: 486px;
    background: radial-gradient(ellipse at 40% 45%, #e9ded8 0%, #f1ebe7 45%, #ffffff 85%);
  }
  .desk-photo {
    position: absolute; left: 0; top: 542px; width: 875px; height: 658px;
    background:
      radial-gradient(ellipse at 78% 35%, #efe7e4 0%, rgba(255,255,255,0) 55%),
      radial-gradient(ellipse at 65% 95%, #eee4df 0%, rgba(255,255,255,0) 50%),
      linear-gradient(180deg, #fbf8f7 0%, var(--mist) 100%);
  }
  .tagline { position: absolute; left: 0; top: 0; width: 875px; height: 270px; font-size: 43px; }
  .tagline .line { position: absolute; left: 342px; line-height: 52px; white-space: nowrap; }
  .tagline .l1 { top: 19px; }
  .tagline .l2 { top: 99px; }
  .tagline .l3 { top: 160px; }
  .tagline .l4 { top: 212px; }
  .brush {
    position: absolute; left: 304px; top: 80px; width: 460px; height: 86px;
    background: var(--yellow); border-radius: 6px 22px 8px 18px;
  }
  .script {
    position: absolute; left: 425px; top: 84px; line-height: 80px;
    font-family: "Kaushan Script", cursive; color: var(--paper); font-size: 56px; white-space: nowrap;
  }
  .banner {
    position: absolute; left: 0; top: 486px; width: 875px; height: 56px;
    background: linear-gradient(90deg, var(--pink-soft) 0%, var(--pink) 10%, var(--pink) 90%, var(--pink-soft) 100%);
    display: flex; align-items: center; justify-content: center;
    font-family: "Arimo", Arial, sans-serif; font-weight: 700;
    font-size: 37px; color: var(--paper); white-space: nowrap;
  }
  .advantage-title {
    position: absolute; left: 29px; top: 584px; width: 625px; height: 68px;
    font-weight: 700; font-size: 41px; line-height: 54px;
    border-bottom: 2px solid var(--pink); white-space: nowrap;
  }
  .benefits { position: absolute; left: 30px; top: 676px; list-style: none; }
  .benefits li {
    display: flex; align-items: center; gap: 10px;
    font-size: 35px; font-weight: 600; height: 49px; white-space: nowrap;
  }
  .benefits svg { width: 28px; height: 28px; flex: none; }
  .figure { color: var(--pink); font-weight: 700; font-size: 51px; line-height: 49px; }
  .oh-label { position: absolute; left: 23px; top: 846px; font-size: 35px; font-weight: 600; line-height: 44px; }
  .oh-date { position: absolute; left: 23px; top: 882px; font-size: 55px; font-weight: 600; color: var(--pink); line-height: 66px; white-space: nowrap; }
  .oh-info { position: absolute; left: 23px; top: 952px; font-size: 35px; font-weight: 600; line-height: 44px; white-space: nowrap; }
  .contact { position: absolute; left: 23px; top: 1001px; list-style: none; }
  .contact li { display: flex; align-items: center; gap: 12px; font-size: 34px; font-weight: 600; height: 47px; white-space: nowrap; }
  .contact svg { width: 30px; height: 30px; flex: none; }
</style>
</head>
<body>
<main class="ad">
  <div class="hero-photo" role="img" aria-label="Photo of a smiling professional woman working on a laptop in a bright office"></div>
  <div class="desk-photo" role="img" aria-label="Soft, faded photo of a desk with coffee cup, papers and hands writing with a pen"></div>

  <div class="tagline">
    <span class="line l1">A stable, lucrative career,</span>
    <div class="brush" aria-hidden="true"></div>
    <span class="line l2">with</span>
    <span class="script">high-paying,</span>
    <span class="line l3">full /part time opportunities</span>
    <span class="line l4">in Private/Public companies</span>
  </div>

  <h1 class="banner">A MASTER’S DEGREE IN ACCOUNTING</h1>

  <h2 class="advantage-title">The SRA Job Placement advantage :</h2>
  <ul class="benefits">
    <li>
      <svg viewBox="0 0 26 26" aria-hidden="true"><rect x="2" y="4" width="19" height="19" rx="2" fill="none" stroke="#e8616f" stroke-width="2.4"/><path d="M7 13l5 5 11-13" fill="none" stroke="#e8616f" stroke-width="3" stroke-linecap="round" stroke-linejoin="round"/></svg>
      <span><span class="figure">96%</span> Placement Rate</span>
    </li>
    <li>
      <svg viewBox="0 0 26 26" aria-hidden="true"><rect x="2" y="4" width="19" height="19" rx="2" fill="none" stroke="#e8616f" stroke-width="2.4"/><path d="M7 13l5 5 11-13" fill="none" stroke="#e8616f" stroke-width="3" stroke-linecap="round" stroke-linejoin="round"/></svg>
      <span><span class="figure">6</span> placement directors</span>
    </li>
    <li>
      <svg viewBox="0 0 26 26" aria-hidden="true"><rect x="2" y="4" width="19" height="19" rx="2" fill="none" stroke="#e8616f" stroke-width="2.4"/><path d="M7 13l5 5 11-13" fill="none" stroke="#e8616f" stroke-width="3" stroke-linecap="round" stroke-linejoin="round"/></svg>
      <span>decades of relationships with <span class="figure">100</span>’s of firms</span>
    </li>
  </ul>

  <p class="oh-label">Meetwave open house</p>
  <p class="oh-date">Sunday June 14, 2 PM</p>
  <p class="oh-info">for a Meetwave link / conference number / information :</p>
  <ul class="contact">
    <li>
      <svg viewBox="0 0 28 28" aria-hidden="true"><rect x="3" y="7" width="22" height="15" fill="none" stroke="#e8616f" stroke-width="2"/><path d="M3 7l11 9 11-9" fill="none" stroke="#e8616f" stroke-width="2"/></svg>
      <span>info@silverleafrise.org</span>
    </li>
    <li>
      <svg viewBox="0 0 28 28" aria-hidden="true"><rect x="9" y="3" width="11" height="22" rx="2" fill="none" stroke="#e8616f" stroke-width="2"/><line x1="13" y1="21" x2="16" y2="21" stroke="#e8616f" stroke-width="2"/></svg>
      <span>555 014 2200 x 111</span>
    </li>
  </ul>
</main>
</body>
</html>
```